Praxis für Psychotherapie benötigt Corporate Design
Vielen Dank für das Design. Hat mich auch in der Gestaltung meiner Räumlichkeiten noch mal beeinflusst. Danke nochmal, gute Arbeit. Alles Gute Timo Berwald
Zielgruppe
Praxis für Psychotherapie, Patienten im Alter zwischen 18 und 75 Jahren
Aufgabenstellung
1. Der Origami Kranich muss vorkommen (kann stilisiert, geometrisch aber auch gezeichnet oder skelettiert sein).
2. Meine Handskizze beschreibt die ungefähre Richtung, bin aber auch für eine andere Anordnung offen.
3. Ich mag klare Linien, kann mich aber auch für das un- perfekte, schöne im Wabi Sabi begeistern. Daher hätte ich gerne Vorschläge in beide Richtungen.
4. Für die Visitenkarte sollte das Logo auf die Vorderseite, Adresse usw. auf die Rückseite.

```html
<!DOCTYPE html>
<html lang="de">
<head>
<meta charset="utf-8">
<title>Praxis für Psychotherapie Timo Berwald – Geschäftsausstattung</title>
<link href="https://fonts.googleapis.com/css2?family=Noto+Serif:wght@400;700&display=swap" rel="stylesheet">
<style>
:root{
  --navy:#1c2f55;
  --green:#72b529;
  --paper:#ffffff;
  --ground:#f7f5f5;
  --ink:#1c2f55;
}
*{margin:0;padding:0;box-sizing:border-box}
html,body{width:1200px;height:720px;overflow:hidden;background:var(--ground)}
body{position:relative;font-family:"Noto Serif",Georgia,serif;color:var(--ink)}
.sheet{position:absolute;background:var(--paper)}
.abs{position:absolute;white-space:nowrap;line-height:1}
.tagline{color:var(--green);font-weight:400}
.wordmark{font-variant:small-caps;font-weight:400;color:var(--navy);letter-spacing:.02em}
.mark-circle{position:absolute;border-radius:50%;border:1.4px solid var(--navy)}
.contact-list{list-style:none}
.contact-list li{display:flex;align-items:center;gap:5px}
.icon{width:7px;height:7px;flex:none}

/* card front */
.card-front{left:300px;top:301px;width:206px;height:130px}
.card-front .band{position:absolute;left:0;right:0;bottom:0;height:3px;background:var(--green)}
.card-front .tagline{left:14px;top:13px;font-size:6px}
.card-front .wordmark{left:13px;top:20px;font-size:14.5px}
.card-front .address{left:115px;top:64px;font-size:5.6px;line-height:8px;white-space:normal}
.card-front .contact-list{position:absolute;left:118px;top:88px;font-size:5.6px}
.card-front .contact-list li{height:8px;gap:4px}
.card-front .contact-list .icon{width:5.5px;height:5.5px}
.card-front .hours{left:15px;top:96px;font-size:5.6px;line-height:7.5px;white-space:normal}
.hours strong{font-weight:700}

/* card back */
.card-back{left:300px;top:493px;width:205px;height:131px;background:var(--navy)}
.card-back .mark-circle{left:31px;top:46px;width:40px;height:40px;border-color:#fff}
.card-back .tagline{left:79px;top:50px;font-size:6.6px}
.card-back .wordmark{left:79px;top:57px;font-size:16px;color:#fff}

/* letterhead */
.letter{left:545px;top:86px;width:384px;height:540px}
.letter .mark-circle{left:200px;top:15px;width:44px;height:44px}
.letter .tagline{left:254px;top:24px;font-size:7.8px}
.letter .wordmark{left:253px;top:32px;font-size:18px}
.letter .sender{left:44px;top:107px;font-size:3.6px;color:var(--navy)}
.sender b{font-weight:700}
.sender span{color:var(--navy);opacity:.85}
.letter .rule{position:absolute;left:246px;top:97px;width:1px;height:119px;background:var(--green)}
.letter .contact-list{position:absolute;left:252px;top:97px;font-size:6.6px}
.letter .contact-list li{height:9.2px;gap:5px}
.letter .info{left:252px;font-size:6.6px;line-height:9px;white-space:normal}
.info strong{font-weight:700}
.info .bank-key{display:inline-block;width:22px;font-weight:700}
</style>
</head>
<body>

<svg width="0" height="0" style="position:absolute" aria-hidden="true">
  <defs>
    <symbol id="ico-phone" viewBox="0 0 10 10"><circle cx="5" cy="5" r="5" fill="#72b529"/><path d="M3.2 2.6c.3-.3.7-.2.9.1l.5.8c.1.2 0 .4-.1.6l-.3.3c.3.7.8 1.2 1.5 1.5l.3-.3c.2-.1.4-.2.6-.1l.8.5c.3.2.4.6.1.9l-.4.4c-.4.4-1.3.3-2.4-.5-.9-.7-1.6-1.5-2-2.4-.3-.8-.2-1.5.1-1.8z" fill="#fff"/></symbol>
    <symbol id="ico-fax" viewBox="0 0 10 10"><circle cx="5" cy="5" r="5" fill="#72b529"/><rect x="3" y="4" width="4" height="3" fill="#fff"/><rect x="3.6" y="2.6" width="2.8" height="1.6" fill="none" stroke="#fff" stroke-width=".6"/></symbol>
    <symbol id="ico-mail" viewBox="0 0 10 10"><circle cx="5" cy="5" r="5" fill="#72b529"/><rect x="2.8" y="3.5" width="4.4" height="3" fill="#fff"/><path d="M2.8 3.5L5 5.2 7.2 3.5" fill="none" stroke="#72b529" stroke-width=".5"/></symbol>
    <symbol id="ico-web" viewBox="0 0 10 10"><circle cx="5" cy="5" r="5" fill="#72b529"/><circle cx="5" cy="5" r="2.4" fill="none" stroke="#fff" stroke-width=".6"/><path d="M2.6 5h4.8M5 2.6v4.8" stroke="#fff" stroke-width=".5"/></symbol>
  </defs>
</svg>

<!-- Visitenkarte Rückseite: Kontakt -->
<section class="sheet card-front" aria-label="Visitenkarte Kontaktseite">
  <p class="abs tagline">Praxis für Psychotherapie</p>
  <p class="abs wordmark">Timo Berwald</p>
  <p class="abs address">Lindenweg 14<br>37412 Harzhofen</p>
  <ul class="contact-list">
    <li><svg class="icon"><use href="#ico-phone"/></svg>+49 (0) 5521 48-0</li>
    <li><svg class="icon"><use href="#ico-fax"/></svg>+49 (0) 5521 48-172</li>
    <li><svg class="icon"><use href="#ico-mail"/></svg>info@timo-berwald.de</li>
    <li><svg class="icon"><use href="#ico-web"/></svg>www.timo-berwald.de</li>
  </ul>
  <p class="abs hours"><strong>Sprechstunden:</strong><br>Mo - Fr 8 - 11 &amp; 16 - 17 Uhr<br>&amp; nach Vereinbarung</p>
  <div class="band"></div>
</section>

<!-- Visitenkarte Vorderseite: Logo -->
<section class="sheet card-back" aria-label="Visitenkarte Logoseite">
  <span class="mark-circle"></span>
  <p class="abs tagline">Praxis für Psychotherapie</p>
  <p class="abs wordmark">Timo Berwald</p>
</section>

<!-- Briefbogen -->
<section class="sheet letter" aria-label="Briefbogen">
  <span class="mark-circle"></span>
  <p class="abs tagline">Praxis für Psychotherapie</p>
  <p class="abs wordmark">Timo Berwald</p>

  <p class="abs sender"><b>Praxis für Psychotherapie Timo Berwald</b> <span>• Lindenweg 14 • 37412 Harzhofen</span></p>

  <div class="rule"></div>
  <ul class="contact-list">
    <li><svg class="icon"><use href="#ico-phone"/></svg>+49 (0) 5521 48-0</li>
    <li><svg class="icon"><use href="#ico-fax"/></svg>+49 (0) 5521 48-172</li>
    <li><svg class="icon"><use href="#ico-mail"/></svg>info@timo-berwald.de</li>
    <li><svg class="icon"><use href="#ico-web"/></svg>www.timo-berwald.de</li>
  </ul>
  <p class="abs info" style="top:142px"><strong>Timo Berwald</strong><br>Psychologischer<br>Psychotherapeut</p>
  <p class="abs info" style="top:177px;line-height:8px">Kreisbank Harzhofen<br><span class="bank-key">IBAN</span>DE 00 0000 0000 0000 0000 00<br><span class="bank-key">BIC</span>KRHZDE21XXX</p>
  <p class="abs info" style="top:210px">USt-IdNr.: DE 000000000</p>
</section>

</body>
</html>
```